R.Tamo Fiji Limited

to create a master letter head with 35 years of fijian owned
Company boilerplate (for proposals/emails)
R. Tamo Fiji Limited is a respected Fijian company with 35 years of continuous service to our communities across the Pacific. We deliver end-to-end manufacturing and engineering, commercial refrigeration & air-conditioning, property development/management, and mobility solutions. As a distributor of B-L-UP golf carts and Norvex batteries, we support resorts, airports, and industries with reliable supply, parts, and after-sales service. Built on craftsmanship, integrity, and community, R. Tamo has become a household name in Fiji.
About-us paragraph (website “About”)
For 35 years, R. Tamo Fiji Limited has been a pillar of the local economy and a trusted partner throughout the Pacific Islands. Our group combines precision manufacturing and stainless-steel fabrication with refrigeration & air-conditioning projects, real-estate development, and golf-cart fleets and energy systems. We proudly distribute B-L-UP golf carts and Norvex batteries, and we back every sale with responsive technical support. Our promise is simple: reliable quality, fair value, and long-term support for every client.
Industry/Entity Type
Group Buiness

```html
<!DOCTYPE html>
<html lang="en">
<head>
<meta charset="utf-8">
<title>R.Tamo Fiji Limited – Letterhead</title>
<link rel="stylesheet" href="https://fonts.googleapis.com/css2?family=Source+Sans+3:wght@400;600;700&display=swap">
<style>
  :root {
    --paper: #ffffff;
    --navy: #1d3d6e;
    --ink: #4a4a4c;
    --ink-strong: #3b3b3d;
    --signature-tone: #e7e7ea;
  }
  * { margin: 0; padding: 0; box-sizing: border-box; }
  html, body { width: 964px; height: 1200px; overflow: hidden; background: var(--paper); }
  .letterhead {
    position: relative;
    width: 964px;
    height: 1200px;
    background: var(--paper);
    font-family: "Source Sans 3", "Myriad Pro", Arial, sans-serif;
    color: var(--ink);
  }
  .brand {
    position: absolute;
    left: 91px;
    top: 84px;
    display: flex;
    align-items: center;
    gap: 12px;
    color: var(--navy);
    font-weight: 700;
    font-size: 40px;
    letter-spacing: 1px;
    line-height: 1;
  }
  .brand-dot {
    width: 14px; height: 14px; border-radius: 50%; background: var(--navy);
  }
  .contact {
    position: absolute;
    left: 705px;
    top: 62px;
    font-size: 14.5px;
    line-height: 17px;
    color: var(--ink);
  }
  .contact-address { margin-bottom: 7px; }
  .contact-line { display: flex; align-items: center; gap: 10px; height: 17px; }
  .contact-line svg { width: 12px; height: 12px; fill: var(--navy); flex: none; }
  .letter-date {
    position: absolute;
    left: 93px;
    top: 303px;
    font-size: 16.5px;
    font-weight: 600;
    color: var(--ink-strong);
  }
  .recipient {
    position: absolute;
    left: 93px;
    top: 364px;
    font-size: 16.5px;
    font-weight: 600;
    line-height: 20.5px;
    color: var(--ink-strong);
  }
  .letter-body {
    position: absolute;
    left: 91px;
    top: 482px;
    width: 779px;
    font-size: 14.6px;
    line-height: 20.5px;
    text-align: justify;
    color: var(--ink);
  }
  .letter-body p + p { margin-top: 20.5px; }
  .letter-body p:last-child { text-align: left; }
  .signature-mark {
    position: absolute;
    left: 694px;
    top: 900px;
    width: 150px;
    height: 58px;
    background: var(--signature-tone);
  }
  .signatory-title {
    position: absolute;
    left: 732px;
    top: 955px;
    font-size: 14.5px;
    color: var(--ink);
  }
</style>
</head>
<body>
<main class="letterhead">
  <header>
    <div class="brand"><span class="brand-dot"></span><span class="brand-name">R.TAMO FIJI</span></div>
    <address class="contact" style="font-style:normal">
      <div class="contact-address">4810 Harbour View Road<br>Lami Bay, FJ 20418</div>
      <div class="contact-line">
        <svg viewBox="0 0 24 24" aria-hidden="true"><path d="M6.6 10.8a15.1 15.1 0 0 0 6.6 6.6l2.2-2.2a1 1 0 0 1 1-.25 11.4 11.4 0 0 0 3.6.57 1 1 0 0 1 1 1V20a1 1 0 0 1-1 1A17 17 0 0 1 3 4a1 1 0 0 1 1-1h3.5a1 1 0 0 1 1 1c0 1.25.2 2.45.57 3.57a1 1 0 0 1-.25 1z"/></svg>
        <span>679-330-5182</span>
      </div>
      <div class="contact-line">
        <svg viewBox="0 0 24 24" aria-hidden="true"><path d="M2 5h20v14H2z M2 5l10 8 10-8" fill="none" stroke="#1d3d6e" stroke-width="0"/><path d="M2 5h20v2l-10 7L2 7z"/><path d="M2 9l10 7 10-7v10H2z"/></svg>
        <span>info@RTamo.com</span>
      </div>
      <div class="contact-line">
        <svg viewBox="0 0 24 24" aria-hidden="true"><circle cx="12" cy="12" r="10"/><path d="M2 12h20M12 2c3 3 3 17 0 20M12 2c-3 3-3 17 0 20" stroke="#fff" stroke-width="1.6" fill="none"/></svg>
        <span>www.RTamo.com</span>
      </div>
    </address>
  </header>

  <p class="letter-date">Cartagena de Indias, Ocober 12,2015</p>

  <div class="recipient">
    Sr.<br>ANDRES MOLINA<br>Web Master<br>City
  </div>

  <section class="letter-body">
    <p>Contrary to popular belief, Lorem Ipsum is not simply random text. It has roots in a piece of classical Latin literature from 45 BC, making it over 2000 years old. Edmund Hale, a Latin professor at Ashford-Bayley College in Virginia, looked up one of the more obscure Latin words, consectetur, from a Lorem Ipsum passage, and going through the cites of the word in classical literature,</p>
    <p>discovered the undoubtable source. Lorem Ipsum comes from sections 1.10.32 and 1.10.33 of "de Finibus Bonorum et Malorum" (The Extremes of Good and Evil) by Aurelian, written in 45 BC. This book is a treatise on the theory of ethics, very popular during the Renaissance. The first line of Lorem Ipsum, "Lorem ipsum dolor sit amet..", comes from a line in section 1.10.32.</p>
    <p>The standard chunk of Lorem Ipsum used since the 1500s is reproduced below for those interested. Sections 1.10.32 and 1.10.33 from "de Finibus Bonorum et Malorum" by Aurelian are also reproduced in their exact original form, accompanied by English versions from the 1914 translation by H. Rowley.</p>
    <p>There are many variations of passages of Lorem Ipsum available, but the majority have suffered alteration in some form, by injected humour, or randomised words which don't look even slightly believable. If you are going to use a passage of Lorem Ipsum, you need to be sure there isn't anything embarrassing hidden in the middle of text. All the Lorem Ipsum generators o</p>
  </section>

  <div class="signature-mark" role="img" aria-label="Handwritten signature of Tomas Reva"></div>
  <p class="signatory-title">CEO/ FOUNDER</p>
</main>
</body>
</html>
```